Enhancement Of Draft Website - www.skylarkvolt.com

The website www.skylarkvolt.com exists but needs further development. With the exception of a small number of pages, the website is populated with the majority of content it requires. I would like a designer to review the design of the website and propose an enhanced design paying particular consideration to the following:

-Setting an appropriate colour scheme that matches with the company logo
-Ensuring the company logo is displayed appropriately on the website
-Making any other appropriate adjustments (through the selection of another theme / the customisation of the existing template) that improve the experience of the user on the website

An XML export file from the existing website is attached.

Target Market(s)

Specialist website targeting engineers working in aerospace companies

Industry/Entity Type

Engineer

Font styles to use
Sans Serif

Requirements
Must have
• Responsive design working across platforms. Contact form. Ease of use.

```html
<!DOCTYPE html>
<html lang="en">
<head>
<meta charset="utf-8">
<title>SkylarkVolt – High Voltage Engineering</title>
<link href="https://fonts.googleapis.com/css2?family=Roboto:wght@400;500;700&family=Oswald:wght@400;500&display=swap" rel="stylesheet">
<style>
:root{
  --brand:#3b6b99;
  --brand-dark:#2d5b86;
  --band:#4b5664;
  --footer:#2c2c2c;
  --footer-deep:#262626;
  --ink:#222;
  --white:#fff;
  --muted:#cfd6de;
}
*{margin:0;padding:0;box-sizing:border-box}
html,body{width:800px;height:1200px;overflow:hidden}
body{font-family:'Roboto',sans-serif;color:var(--ink);background:var(--white);position:relative}
.topbar{height:25px;background:var(--brand);color:var(--white);font-size:9px;display:flex;align-items:center;padding:0 60px;gap:14px}
.topbar .spacer{flex:1}
.topbar .social{display:flex;gap:4px;border-left:1px solid rgba(255,255,255,.3);padding-left:14px;height:25px;align-items:center}
.topbar .social span{width:9px;height:9px;background:var(--white);border-radius:2px}
.header{height:58px;display:flex;align-items:center;padding:0 57px 0 60px}
.brand{display:flex;align-items:center;gap:8px;font-size:20px;font-weight:500;color:var(--brand-dark)}
.brand .mark{width:26px;height:24px;background:var(--brand-dark)}
.nav{margin-left:auto;display:flex;gap:25px;font-size:10px;letter-spacing:.2px}
.nav a{color:var(--ink);text-decoration:none}
.nav a.active{color:var(--brand)}
.hero{position:absolute;top:83px;left:0;width:800px;height:384px;background:radial-gradient(ellipse at 50% 40%,#5c6b7e 0%,#3a4656 55%,#1e252f 100%)}
.hero h1{position:absolute;top:140px;width:100%;text-align:center;font-family:'Oswald',sans-serif;font-weight:500;font-size:38px;color:var(--white);text-shadow:0 2px 4px rgba(0,0,0,.5)}
.hero p{position:absolute;top:192px;width:100%;text-align:center;font-family:'Oswald',sans-serif;font-size:19px;color:var(--white);text-shadow:0 2px 4px rgba(0,0,0,.5)}
.hero .arrow{position:absolute;top:178px;width:20px;height:20px;border-radius:50%;background:rgba(0,0,0,.6)}
.services{position:absolute;top:467px;left:0;width:800px;height:287px;background:linear-gradient(135deg,#2f5c87,#3a6c9c 50%,#2d5a85);color:var(--white);text-align:center}
.services h2{margin-top:42px;font-size:19px;font-weight:500}
.svc{position:absolute;top:90px;width:220px;text-align:center}
.svc .icon{width:62px;height:62px;margin:0 auto;display:block}
.svc h3{margin-top:19px;font-size:14px;font-weight:400;letter-spacing:.3px}
.svc p{margin-top:10px;font-size:9px;line-height:13px}
.svc .more{display:block;margin-top:12px;font-size:9px}
.basics-band{position:absolute;top:754px;left:0;width:800px;height:62px;background:var(--band);color:var(--white);text-align:center;font-size:19px;font-weight:500;line-height:62px}
.tiles{position:absolute;top:816px;left:0;width:800px;height:196px;display:flex}
.tile{width:200px;height:196px;position:relative}
.tile .cap{position:absolute;bottom:0;left:0;width:100%;height:31px;background:rgba(30,30,30,.55);color:var(--white);font-size:13.5px;font-weight:500;text-align:center;line-height:31px}
.footer{position:absolute;top:1012px;left:0;width:800px;height:141px;background:var(--footer);color:var(--white)}
.col{position:absolute;top:27px}
.col h4{font-size:12px;font-weight:400;letter-spacing:.2px;margin-bottom:14px}
.col p{font-size:8px;line-height:13px;color:#e6e6e6}
.contact-line{display:flex;align-items:center;gap:9px;font-size:11px;margin-top:6px}
.contact-line.small{font-size:8.5px}
.signup{display:flex;margin-top:14px}
.signup .field{width:114px;height:28px;background:var(--white);font-size:7px;color:#999;padding-left:9px;line-height:28px}
.signup .btn{width:54px;height:28px;background:var(--brand);font-size:10px;text-align:center;line-height:28px}
.socials{display:flex;gap:12px}
.socials span{width:23px;height:23px;background:#f2f2f2;border-radius:2px}
.copyright{position:absolute;top:1153px;left:0;width:800px;height:47px;background:var(--footer-deep);border-top:1px solid #3a3a3a;color:#ddd;font-size:9px;text-align:center;line-height:46px}
</style>
</head>
<body>
<div class="topbar">
  <span>☎ : 0810455</span><span>✉ : info@skylarkvolt.com</span>
  <span class="spacer"></span>
  <svg width="10" height="10" viewBox="0 0 10 10"><circle cx="4" cy="4" r="3" fill="none" stroke="#fff" stroke-width="1.4"/><line x1="6.2" y1="6.2" x2="9" y2="9" stroke="#fff" stroke-width="1.4"/></svg>
  <div class="social"><span></span><span></span><span></span><span></span></div>
</div>
<header class="header">
  <div class="brand"><span class="mark"></span>SkylarkVolt</div>
  <nav class="nav">
    <a class="active" href="#">HOME</a><a href="#">ENGINEERING</a><a href="#">TESTING</a><a href="#">TRAINING</a><a href="#">HV BASICS</a><a href="#">ABOUT US</a><a href="#">CONTACT US</a>
  </nav>
</header>
<section class="hero" role="img" aria-label="Photo of an electric arc between two dark spherical electrodes">
  <h1>HIGH VOLTAGE TRAINING</h1>
  <p>Operation and maintenance of HV systems</p>
  <span class="arrow" style="left:39px"><svg width="20" height="20" viewBox="0 0 20 20"><path d="M11.5 6 7.5 10l4 4" fill="none" stroke="#fff" stroke-width="1.5"/></svg></span>
  <span class="arrow" style="left:744px"><svg width="20" height="20" viewBox="0 0 20 20"><path d="M8.5 6l4 4-4 4" fill="none" stroke="#fff" stroke-width="1.5"/></svg></span>
</section>
<section class="services">
  <h2>OUR SERVICES</h2>
  <div class="svc" style="left:60px">
    <svg class="icon" viewBox="0 0 62 62"><path d="M8 1h62l-8 61H0z" transform="translate(-4 0) scale(1 .98)" fill="none" stroke="#fff" stroke-width="1"/><circle cx="27" cy="35" r="7" fill="none" stroke="#fff" stroke-width="4" stroke-dasharray="3 2"/><circle cx="38" cy="25" r="4" fill="none" stroke="#fff" stroke-width="3" stroke-dasharray="2 1.5"/><circle cx="39" cy="40" r="3.5" fill="none" stroke="#fff" stroke-width="3" stroke-dasharray="2 1.5"/></svg>
    <h3>ENGINEERING</h3>
    <p>Supporting the design of new HV systems and<br>components for use in aerospace environments</p>
    <span class="more">Learn More -&gt;</span>
  </div>
  <div class="svc" style="left:297px">
    <svg class="icon" viewBox="0 0 62 62"><path d="M4 1h62l-8 60H-4z" fill="none" stroke="#fff" stroke-width="1"/><path d="M33 18l-9 14h7l-3 13 9-16h-7z" fill="#fff"/></svg>
    <h3>TESTING</h3>
    <p>Access to a full range of testing services to<br>validate the performance of HV systems</p>
    <span class="more">Learn More -&gt;</span>
  </div>
  <div class="svc" style="left:532px">
    <svg class="icon" viewBox="0 0 62 62"><path d="M4 1h62l-8 60H-4z" fill="none" stroke="#fff" stroke-width="1"/><circle cx="31" cy="24" r="5" fill="#fff"/><circle cx="22" cy="27" r="3.5" fill="#fff"/><circle cx="40" cy="27" r="3.5" fill="#fff"/><path d="M23 42c0-7 3-10 8-10s8 3 8 10zM15 39c0-5 2-7 6-7l2 1-1 6zM47 39c0-5-2-7-6-7l-2 1 1 6z" fill="#fff"/></svg>
    <h3>TRAINING</h3>
    <p>Online and face to face training provision to<br>support your workforce</p>
    <span class="more">Learn More -&gt;</span>
  </div>
</section>
<div class="basics-band">HV BASICS</div>
<section class="tiles">
  <div class="tile" role="img" aria-label="Photo of connector pins on a circuit board" style="background:linear-gradient(135deg,#3a3f46,#8a8f95 45%,#2a6fb8)"><span class="cap">CLEARANCES</span></div>
  <div class="tile" role="img" aria-label="Photo of a terminal block with wired connectors" style="background:linear-gradient(180deg,#c9c9c9,#9a9d9f 50%,#4a4d50)"><span class="cap">ELECTRICAL DISCHARGE</span></div>
  <div class="tile" role="img" aria-label="Photo of a blue lightning discharge" style="background:radial-gradient(ellipse at 50% 50%,#8a90ff,#3b3fb0 45%,#151a4a)"><span class="cap">PARTIAL DISCHARGE</span></div>
  <div class="tile" role="img" aria-label="Photo of a hand operating a test instrument" style="background:linear-gradient(135deg,#1d8fd0,#2c5e9e 55%,#d8b9ac)"><span class="cap">HV TESTING</span></div>
</section>
<footer class="footer">
  <div class="col" style="left:60px">
    <h4>CONTACT US</h4>
    <p>48 Birch Lane Fairview NJ 07022<br>215 Ridge Avenue Suite 4<br>Fairview NJ 07022</p>
    <div class="contact-line"><svg width="13" height="13" viewBox="0 0 13 13"><path d="M2 1l3 3-1.5 1.5c1 2 2 3 4 4L9 8l3 3-2 2C5 12 1 8 0 3z" fill="none" stroke="#fff" stroke-width=".9"/></svg>0810455</div>
    <div class="contact-line small"><svg width="13" height="10" viewBox="0 0 13 10"><rect x=".5" y=".5" width="12" height="9" fill="none" stroke="#fff"/><path d="M.5.5l6 5 6-5" fill="none" stroke="#fff"/></svg>info@skylarkvolt.com</div>
  </div>
  <div class="col" style="left:243px;width:165px">
    <h4>SKYLARK VOLT</h4>
    <p style="font-size:7.3px;line-height:12.2px;text-align:justify">SkylarkVolt can provide you with the engineering support you require as you develop new high voltage components and systems. With experience of cabling, connectors, electrical machines and power electronics we can help identify</p>
  </div>
  <div class="col" style="left:453px;width:170px">
    <h4>NEWSLETTER</h4>
    <p style="font-size:7.5px;line-height:14px">Excepteur sint occaecat cupidatat non proident, sunt in culpa qui officia deserunt mollit anim</p>
    <div class="signup"><span class="field">Enter your email address</span><span class="btn">Sign Up</span></div>
  </div>
  <div class="col" style="left:651px">
    <h4>SOCIAL MEDIA</h4>
    <div class="socials"><span></span><span></span><span></span></div>
  </div>
</footer>
<div class="copyright">2016 &nbsp;All Rights Reserved.</div>
</body>
</html>
```